Bref créative
Lark Hollow Events Business Cards & Stationary
A focus on events. All of them. All aspects of them. Anywhere.
I need double sided standard sized Business Card [3.5" x 2"]
Century Gothic
Professional
Melissa Dorne
CEO or would also like to try putting a function like "meetings + events"
4172 County Road 208
Alder Falls, MN 55099
melissa@larkhollowevents.example
www.larkhollowevents.example
Info on who we are and what we do can be found on our website at www.larkhollowevents.example
Would like to see different options like:
phone.
cell.
email.
also, would like to see some options with this symbol: |
Like:
melissa dorne | lark hollow events
Would like to see the card with and without title.
Also, like the + symbol.
I'd like our business cards to look hip and professional...but want them to have some personality.
Our branding colors are gray, teal, and white. Open to incorporting another sub color as you see fit--possibly taupe, navy, or dark fuscia.
Hoping to see innovative ideas on what is up-and-coming with business cards now for people to take notice.
Our logo is new so we are interested in unique ways to use it.
I would like to try to fit this explanation about our name on the back because I love it. I know this will be tight--do what you need to if you need to cut out a little to get it to fit....but lets see if we can do this on the back. (Or, we could go to the fold-out kind if we have to and then do ubllets of our services on the back.)
In the 1950’s, doctors developed a personality classification that was supposed to help them identify predicators for heart disease. They grouped certain criteria together and labeled that personality, “Type A”. The term has come to have some negative connotations.
From our point of view, while we are an eclectic team of varied personalities and interests, we endeavor to provide type A service.
Does that make us a group of unlikable, over-bearing maniacs? No.
We think the so-called “symptoms” of type A are the same qualifications you want in your event planners:
Type A individuals can be described as time-conscious, competitive, ambitious, business-like perfectionists. They are usually over-achievers who derive a great deal of satisfaction from work and multi-tasking. They drive themselves with deadlines and are often “stress junkies”.
–Quiet Engines: Habits of the Restless Mind, Harold Vance
We proudly don the scarlet letter as a badge of our undying need to deliver services to you on time, in budget, and beyond your expectations. If that ends up leading to heart disease….well, we’ll live with that. If our service prevents your heart attacks, then we’ve done our job.
The colors of the logos are very close but still not quite hitting the mark--the gray is a little greenish and the teal is a little blah. When you're using them, please try other shades of gray and teal.
here is the eps version instead of ai in case that is desireable

```html
<!DOCTYPE html>
<html lang="en">
<head>
<meta charset="utf-8">
<title>Lark Hollow Events — Stationery Set</title>
<link href="https://fonts.googleapis.com/css2?family=Didact+Gothic&display=swap" rel="stylesheet">
<style>
  :root {
    --backdrop: #d6d6d6;
    --paper: #ffffff;
    --ink-dark: #4a463f;
    --ink-text: #5a5650;
    --ink-soft: #8a867f;
    --ink-on-dark: #e6e3dc;
    --mark-faint: #5c584f;
  }
  * { box-sizing: border-box; margin: 0; padding: 0; }
  html, body { width: 1200px; height: 682px; overflow: hidden; }
  body {
    background: var(--backdrop);
    font-family: "Didact Gothic", "Century Gothic", sans-serif;
    color: var(--ink-text);
    position: relative;
  }
  .sheet {
    position: absolute;
    background: var(--paper);
    box-shadow: 0 1px 3px rgba(0,0,0,0.18);
    overflow: hidden;
  }
  .brand-name {
    font-size: 13px;
    letter-spacing: 0.12em;
    text-transform: uppercase;
    color: var(--ink-dark);
    display: flex;
    align-items: center;
    gap: 7px;
    white-space: nowrap;
  }
  .brand-dot {
    width: 9px; height: 9px;
    border-radius: 50%;
    background: var(--ink-dark);
    flex: none;
  }
  .fine { font-size: 6.5px; line-height: 1.5; color: var(--ink-text); white-space: nowrap; }
  .footer-band {
    position: absolute; left: 0; right: 0; bottom: 0;
    background: var(--ink-dark);
    color: var(--ink-on-dark);
    font-size: 6px;
    padding: 0 14px;
    display: flex; align-items: center;
    white-space: nowrap;
  }
  .contact-list { list-style: none; }
  .contact-list li { display: flex; gap: 6px; }
  .contact-list .label { width: 18px; }

  /* Letterhead */
  .letterhead { left: 187px; top: 19px; width: 452px; height: 634px; }
  .letterhead .brand { position: absolute; left: 30px; top: 92px; }
  .letterhead .top-email { position: absolute; right: 30px; top: 26px; }
  .letterhead .address { position: absolute; left: 30px; bottom: 36px; }
  .letterhead .contact-list { position: absolute; right: 30px; bottom: 30px; }
  .letterhead .footer-band { height: 16px; }

  /* Business card back */
  .card-back {
    left: 34px; top: 222px; width: 138px; height: 76px;
    background: var(--ink-dark);
    padding: 7px 8px;
  }
  .card-back p {
    font-size: 4.2px; line-height: 1.45;
    color: var(--ink-on-dark);
    margin-bottom: 3px;
  }

  /* Business card front */
  .card-front { left: 34px; top: 306px; width: 138px; height: 78px; }
  .card-front .brand { position: absolute; left: 9px; top: 26px; }
  .card-front .brand-name { font-size: 6px; gap: 4px; }
  .card-front .brand-dot { width: 5px; height: 5px; }
  .card-front .person { position: absolute; right: 9px; top: 10px; text-align: right; }
  .card-front .person-name { font-size: 6px; color: var(--ink-dark); }
  .card-front .person-title { font-size: 4.5px; color: var(--ink-soft); }
  .card-front .contact-list { position: absolute; right: 9px; top: 44px; font-size: 4.2px; line-height: 1.5; }
  .card-front .contact-list .label { width: 12px; }
  .card-front .footer-band { height: 8px; font-size: 3.8px; padding: 0 9px; }

  /* Envelope back */
  .envelope-back { left: 684px; top: 60px; width: 487px; height: 228px; }
  .envelope-back .flap { position: absolute; left: 0; top: 0; width: 100%; height: 132px; }
  .envelope-back .flap-mark {
    position: absolute; left: 0; right: 0; top: 70px;
    display: flex; justify-content: center;
  }
  .envelope-back .flap-mark .brand-name { color: var(--mark-faint); font-size: 11px; }
  .envelope-back .flap-mark .brand-dot { background: var(--mark-faint); }

  /* Envelope front */
  .envelope-front { left: 684px; top: 355px; width: 487px; height: 285px; }
  .envelope-front .brand { position: absolute; left: 34px; top: 54px; }
  .envelope-front .address { position: absolute; left: 34px; bottom: 26px; }
  .envelope-front .contact-list { position: absolute; right: 26px; bottom: 22px; }
  .envelope-front .footer-band { height: 12px; }
</style>
</head>
<body>

  <section class="sheet letterhead" aria-label="Letterhead">
    <p class="fine top-email">melissa@larkhollowevents.example</p>
    <div class="brand"><span class="brand-name"><span class="brand-dot"></span>Lark Hollow Events</span></div>
    <p class="fine address">4172 County Road 208 &nbsp;Alder Falls, MN 55099</p>
    <ul class="fine contact-list">
      <li><span class="label">TEL</span><span>555.010.0142</span></li>
      <li><span class="label">CELL</span><span>555.010.0187</span></li>
      <li><span class="label">FAX</span><span>555.010.0199</span></li>
    </ul>
    <div class="footer-band">www.larkhollowevents.example</div>
  </section>

  <section class="sheet card-back" aria-label="Business card, back">
    <p>We plan events of every kind, with calm focus and care.</p>
    <p>Our team is varied in taste yet steady in service.</p>
    <p>Time-conscious, driven, precise: the traits you want in a planner.</p>
    <p>On time, in budget, beyond what you expected.</p>
    <p>Learn more about us online.</p>
  </section>

  <section class="sheet card-front" aria-label="Business card, front">
    <div class="person">
      <p class="person-name">Melissa Dorne</p>
      <p class="person-title">CEO</p>
    </div>
    <div class="brand"><span class="brand-name"><span class="brand-dot"></span>Lark Hollow Events</span></div>
    <ul class="contact-list">
      <li><span class="label">phone.</span><span>555.010.0142</span></li>
      <li><span class="label">cell.</span><span>555.010.0187</span></li>
    </ul>
    <div class="footer-band">www.larkhollowevents.example</div>
  </section>

  <section class="sheet envelope-back" aria-label="Envelope, back">
    <svg class="flap" viewBox="0 0 487 132" preserveAspectRatio="none" aria-hidden="true">
      <path d="M0 0 H487 V96 Q487 104 470 106 Q243.5 140 17 106 Q0 104 0 96 Z" fill="var(--ink-dark)"/>
    </svg>
    <div class="flap-mark"><span class="brand-name"><span class="brand-dot"></span>Lark Hollow Events</span></div>
  </section>

  <section class="sheet envelope-front" aria-label="Envelope, front">
    <div class="brand"><span class="brand-name"><span class="brand-dot"></span>Lark Hollow Events</span></div>
    <p class="fine address">4172 County Road 208 &nbsp;Alder Falls, MN 55099</p>
    <ul class="fine contact-list">
      <li><span class="label">TEL</span><span>555.010.0142</span></li>
      <li><span class="label">CELL</span><span>555.010.0187</span></li>
      <li><span class="label">FAX</span><span>555.010.0199</span></li>
    </ul>
    <div class="footer-band">www.larkhollowevents.example</div>
  </section>

</body>
</html>
```